Business Card and Letterhead for new company Vardel GreenWorks, Inc.

Vardel GreenWorks, Inc., an engineering and construction firm that provides services for solid waste landfill gas systems, needs a business card and letterhead. We recently had a logo designed but we are open to some tweaks to logo design and color scheme. Generally, we like "earthy" color tones - greens, browns, oranges. This is a sister company - www.talvoriengineering.example.

Target Market(s)

Solid waste landfill companies - Brindle Disposal, Halcott Hauling, etc.

Industry/Entity Type

Engineering and Construction

Contact Information for Business Card

Name, Title, email, mobile phone, work phone, website. Potential list of services for back of card: LFG Engineering and Design, GCCS Planning and Operational Consulting, Compliance Monitoring and Reporting, Routine Operations & Maintenance, Nonroutine O&M, Construction Management, Construction QA, GCCS Construction

Font styles to use
Sans Serif

Requirements
Must have
• Logo, pertinent information, maybe a tagline (still in development)
Nice to have
• For back of card, considering an engineering scale (attached for another business of ours), but want to look at other options, alternatives. Like the idea of the back of card to have some utility (scale, unit conversion info, list of services) but willing to consider lots of options.
Should not have
• Needs to have a professional (engineering) and technical look, not cartoonish.

```html
<!DOCTYPE html>
<html lang="en">
<head>
<meta charset="utf-8">
<title>Vardel GreenWorks – Business Card</title>
<link rel="stylesheet" href="https://fonts.googleapis.com/css2?family=Audiowide&family=Fira+Sans:wght@400;500&display=swap">
<style>
  :root {
    --bg: #2b2b2b;
    --card: #ffffff;
    --green: #6cb33f;
    --teal: #1e8fad;
    --ink: #333333;
    --divider: #9a9a9a;
    --flame: #f26a1b;
  }
  * { margin: 0; padding: 0; box-sizing: border-box; }
  html, body { width: 1093px; height: 1200px; overflow: hidden; background: var(--bg); }
  .canvas { position: relative; width: 1093px; height: 1200px; }
  .card {
    position: absolute; left: 265px; width: 580px; height: 356px;
    background: var(--card); border-radius: 30px; overflow: hidden;
  }
  .card--front { top: 226px; }
  .card--back { top: 621px; }

  /* front */
  .brand {
    position: absolute; left: 31px; top: 150px; width: 240px;
    display: flex; align-items: center; gap: 10px;
  }
  .brand__mark { width: 38px; height: 38px; border-radius: 50%; background: var(--green); flex: none; }
  .brand__name {
    font-family: "Audiowide", sans-serif; color: var(--green);
    font-size: 17px; line-height: 1.2; letter-spacing: 0.5px;
  }
  .divider { position: absolute; left: 288px; top: 74px; width: 1px; height: 209px; background: var(--divider); }
  .person { position: absolute; left: 310px; top: 106px; }
  .person__name { font-family: "Audiowide", sans-serif; color: var(--green); font-size: 18px; letter-spacing: 0.5px; }
  .person__title { font-family: "Audiowide", sans-serif; color: var(--teal); font-size: 13px; margin-top: 1px; letter-spacing: 0.4px; }
  .contacts { list-style: none; position: absolute; left: 312px; top: 160px; width: 240px; }
  .contacts li {
    display: flex; align-items: center; gap: 7px; height: 21px;
    font-family: "Fira Sans", sans-serif; font-size: 17px; color: var(--ink);
    white-space: nowrap;
  }
  .contacts svg { width: 15px; height: 15px; flex: none; }

  /* back */
  .ruler { position: absolute; left: 0; top: 0; }
  .ruler text { font-family: "Fira Sans", sans-serif; font-weight: 500; font-size: 15px; fill: var(--green); }
  .services-title {
    position: absolute; left: 48px; top: 158px;
    font-family: "Audiowide", sans-serif; color: var(--green); font-size: 23px; letter-spacing: 0.5px;
  }
  .services { list-style: none; position: absolute; left: 212px; top: 120px; }
  .services li {
    display: flex; align-items: center; gap: 4px; height: 18.3px;
    font-family: "Fira Sans", sans-serif; font-size: 15.5px; color: var(--teal);
    white-space: nowrap;
  }
  .services svg { width: 9px; height: 13px; flex: none; }
</style>
</head>
<body>
<div class="canvas">

  <section class="card card--front">
    <div class="brand">
      <span class="brand__mark"></span>
      <span class="brand__name">VARDEL<br>GREENWORKS</span>
    </div>
    <div class="divider"></div>
    <div class="person">
      <div class="person__name">MARCUS HALE</div>
      <div class="person__title">Managing Director</div>
    </div>
    <ul class="contacts">
      <li><svg viewBox="0 0 16 16"><path d="M4 1.5l2.5 3-1.4 1.7c.8 1.9 2.2 3.3 4.1 4.1l1.7-1.4 3 2.5-1.6 2.6C7 14 2 9 1.4 3.1z" fill="var(--green)"/></svg>044-555 010 237</li>
      <li><svg viewBox="0 0 16 16"><rect x="4" y="1" width="8" height="14" rx="1.5" fill="none" stroke="var(--green)" stroke-width="1.6"/><rect x="7" y="12" width="2" height="1.2" fill="var(--green)"/></svg>044-555 010 238</li>
      <li><svg viewBox="0 0 16 16"><rect x="1" y="3" width="14" height="10" fill="var(--green)"/><path d="M1 3l7 6 7-6" fill="none" stroke="#fff" stroke-width="1.2"/></svg>info@vardelgreen.example</li>
      <li><svg viewBox="0 0 16 16"><g fill="none" stroke="var(--green)" stroke-width="1.2"><circle cx="8" cy="8" r="6.5"/><ellipse cx="8" cy="8" rx="3" ry="6.5"/><path d="M1.5 8h13M2.5 4.8h11M2.5 11.2h11"/></g></svg>www.vardelgreen.example</li>
    </ul>
  </section>

  <section class="card card--back">
    <svg class="ruler" width="580" height="356" viewBox="0 0 580 356" aria-hidden="true">
      <g stroke="var(--green)" stroke-width="1.6">
        <path d="M56.5 2v51M72.2 2v35M87.9 2v35M103.5 2v35M119.2 2v35M134.9 2v51M150.6 2v35M166.3 2v35M181.9 2v35M197.6 2v35M213.3 2v51M229 2v35M244.7 2v35M260.3 2v35M276 2v35M291.7 2v51M307.4 2v35M323.1 2v35M338.7 2v35M354.4 2v35M370.1 2v51M385.8 2v35M401.5 2v35M417.1 2v35M432.8 2v35M448.5 2v51M464.2 2v35M479.9 2v35M495.5 2v35M511.2 2v35M526.9 2v51"/>
        <path d="M56.5 303v51M72.2 319v35M87.9 319v35M103.5 319v35M119.2 319v35M134.9 303v51M150.6 319v35M166.3 319v35M181.9 319v35M197.6 319v35M213.3 303v51M229 319v35M244.7 319v35M260.3 319v35M276 319v35M291.7 303v51M307.4 319v35M323.1 319v35M338.7 319v35M354.4 319v35M370.1 303v51M385.8 319v35M401.5 319v35M417.1 319v35M432.8 319v35M448.5 303v51M464.2 319v35M479.9 319v35M495.5 319v35M511.2 319v35M526.9 303v51"/>
        <path d="M24 77h20M536 83h20M20 272h28M536 278h20"/>
      </g>
      <g text-anchor="middle" dominant-baseline="central">
        <text x="33" y="68">20</text>
        <text x="56.5" y="69">0</text>
        <text x="134.9" y="69">10</text>
        <text x="213.3" y="69">20</text>
        <text x="291.7" y="69">30</text>
        <text x="370.1" y="69">40</text>
        <text x="448.5" y="69">50</text>
        <text x="526.9" y="69">60</text>
        <text x="56.5" y="93" transform="rotate(180 56.5 93)">120</text>
        <text x="134.9" y="93" transform="rotate(180 134.9 93)">100</text>
        <text x="213.3" y="93" transform="rotate(180 213.3 93)">80</text>
        <text x="291.7" y="93" transform="rotate(180 291.7 93)">60</text>
        <text x="370.1" y="93" transform="rotate(180 370.1 93)">40</text>
        <text x="448.5" y="93" transform="rotate(180 448.5 93)">20</text>
        <text x="526.9" y="93">0</text>
        <text x="550" y="93" transform="rotate(180 550 93)">40</text>

        <text x="33" y="263">100</text>
        <text x="56.5" y="264">0</text>
        <text x="213.3" y="264">100</text>
        <text x="370.1" y="264">200</text>
        <text x="526.9" y="264">300</text>
        <text x="56.5" y="288" transform="rotate(180 56.5 288)">150</text>
        <text x="213.3" y="288" transform="rotate(180 213.3 288)">100</text>
        <text x="370.1" y="288" transform="rotate(180 370.1 288)">50</text>
        <text x="526.9" y="288">0</text>
        <text x="550" y="288" transform="rotate(180 550 288)">50</text>
      </g>
    </svg>

    <h2 class="services-title">SERVICES</h2>
    <ul class="services">
      <li><svg viewBox="0 0 9 13"><path d="M4.5 0C6 3 9 5 9 8.5a4.5 4.5 0 0 1-9 0C0 6 2 5 3 3c.5 1 1 1.6 1.5 2z" fill="var(--flame)"/></svg>LFG Engineering and Design</li>
      <li><svg viewBox="0 0 9 13"><path d="M4.5 0C6 3 9 5 9 8.5a4.5 4.5 0 0 1-9 0C0 6 2 5 3 3c.5 1 1 1.6 1.5 2z" fill="var(--flame)"/></svg>GCCS Planning and Operational Consulting</li>
      <li><svg viewBox="0 0 9 13"><path d="M4.5 0C6 3 9 5 9 8.5a4.5 4.5 0 0 1-9 0C0 6 2 5 3 3c.5 1 1 1.6 1.5 2z" fill="var(--flame)"/></svg>Compliance Monitoring and Reporting</li>
      <li><svg viewBox="0 0 9 13"><path d="M4.5 0C6 3 9 5 9 8.5a4.5 4.5 0 0 1-9 0C0 6 2 5 3 3c.5 1 1 1.6 1.5 2z" fill="var(--flame)"/></svg>Routine Operations &amp; Maintenance</li>
      <li><svg viewBox="0 0 9 13"><path d="M4.5 0C6 3 9 5 9 8.5a4.5 4.5 0 0 1-9 0C0 6 2 5 3 3c.5 1 1 1.6 1.5 2z" fill="var(--flame)"/></svg>Nonroutine O&amp;M, Construction Management</li>
      <li><svg viewBox="0 0 9 13"><path d="M4.5 0C6 3 9 5 9 8.5a4.5 4.5 0 0 1-9 0C0 6 2 5 3 3c.5 1 1 1.6 1.5 2z" fill="var(--flame)"/></svg>Construction QA, GCCS Construction</li>
    </ul>
  </section>

</div>
</body>
</html>
```